A simple Chatterbook Ad (not Chatterbook Page) for weight loss surgery

It’s a simple ad in terms of the text.

The text should say:
Curious about weight loss surgery?
This 30 second quiz will tell you which procedure will suit you best

I'm open to variations in the text if it is thought to enhance the ad.

Targeted towards obese individuals who have been unable to lose weight with diet and exercise. My industry is weight loss surgery – webpage www.marcusbellweather.com.au. Clicking the ad leads to a quiz on my webpage relating to weight loss surgery. Most frequent users of this service are females (75%) between ages of 35 and 55 years.

Successful weight loss surgery can enable individuals who have been unable to lose weight to lose a substantial amount of the excess weight they are carrying to be healthier and happier.

```html
<!DOCTYPE html>
<html lang="en">
<head>
<meta charset="utf-8">
<title>Marcus Bellweather – Weight Loss Surgery Quiz Ad</title>
<link rel="stylesheet" href="https://fonts.googleapis.com/css2?family=Montserrat:wght@400;600;900&display=swap">
<style>
  :root {
    --page-bg: #ffffff;
    --teal-deep: #031a18;
    --teal-dark: #07332f;
    --teal-mid: #0f5a53;
    --teal-glow: #1a8a80;
    --accent: #14e0d4;
    --brand-teal: #1a8c82;
    --white: #ffffff;
  }
  * { margin: 0; padding: 0; box-sizing: border-box; }
  html, body {
    width: 1055px;
    height: 1200px;
    overflow: hidden;
    background: var(--page-bg);
  }
  .ad {
    position: absolute;
    left: 77px;
    top: 161px;
    width: 902px;
    height: 894px;
    overflow: hidden;
    font-family: "Montserrat", Arial, sans-serif;
    color: var(--white);
  }
  .ad-backdrop {
    position: absolute;
    inset: 0;
    background:
      radial-gradient(circle at 22% 78%, var(--teal-glow) 0%, transparent 22%),
      radial-gradient(ellipse at 78% 40%, var(--teal-mid) 0%, transparent 55%),
      radial-gradient(ellipse at 20% 25%, var(--teal-mid) 0%, transparent 45%),
      linear-gradient(160deg, var(--teal-dark) 0%, var(--teal-deep) 100%);
  }
  .brand-tab {
    position: absolute;
    left: 189px;
    top: 0;
    width: 501px;
    height: 210px;
    background: var(--white);
    border-radius: 0 0 40px 40px;
    text-align: center;
  }
  .brand-mark {
    position: absolute;
    left: 50%;
    top: 20px;
    width: 76px;
    height: 76px;
    margin-left: -38px;
    border-radius: 50%;
    background: var(--brand-teal);
  }
  .brand-name,
  .brand-role {
    position: absolute;
    left: 0; right: 0;
    line-height: 1;
    font-weight: 600;
    color: var(--brand-teal);
    white-space: nowrap;
  }
  .brand-name {
    top: 135px;
    font-size: 29px;
  }
  .brand-role {
    top: 165px;
    font-size: 10.5px;
    letter-spacing: 1.4px;
    text-transform: uppercase;
  }
  .headline-lead,
  .headline-main,
  .headline-accent,
  .quiz-line {
    position: absolute;
    left: 0; right: 0;
    text-align: center;
    line-height: 1;
    white-space: nowrap;
  }
  .headline-lead {
    top: 296px;
    font-weight: 400;
    font-size: 108px;
    letter-spacing: -0.5px;
  }
  .headline-main {
    top: 412px;
    font-weight: 900;
    font-size: 100px;
    letter-spacing: -1px;
  }
  .headline-accent {
    top: 510px;
    font-weight: 900;
    font-size: 136px;
    letter-spacing: -2px;
    color: var(--accent);
  }
  .quiz-line {
    top: 648px;
    font-weight: 600;
    font-size: 32px;
    line-height: 44px;
  }
</style>
</head>
<body>
  <main class="ad">
    <div class="ad-backdrop" role="img" aria-label="Dark teal background with a large glowing question mark and a faint network-mesh pattern"></div>

    <header class="brand-tab">
      <span class="brand-mark"></span>
      <p class="brand-name">Marcus Bellweather</p>
      <p class="brand-role">General, Upper GI &amp; Bariatric Surgeon</p>
    </header>

    <h1>
      <span class="headline-lead">Curious about</span>
      <span class="headline-main">WEIGHT LOSS</span>
      <span class="headline-accent">SURGERY?</span>
    </h1>

    <p class="quiz-line">This 30 second quiz will tell you which<br>procedure will suit you best</p>
  </main>
</body>
</html>
```